Business Card Design

I need a business card designed for my business.

The company name is Rowan Pellet Group

It has four brands underneath it. They are:
- RP Events
- RP Sports Tours
- RPG Management
- Bold Mosaic

I have attached all logo items, as well as our last business card.

I look forward to seeing your designs.

Industry/Entity Type

Business

Colors
eb1f27
0355a3

Requirements
Must have
• Our contact details as per the front page of our previous business card.

```html
<!DOCTYPE html>
<html lang="en">
<head>
<meta charset="utf-8">
<title>Rowan Pellet Group – Business Card</title>
<link href="https://fonts.googleapis.com/css2?family=Source+Sans+3:wght@400;600;700&display=swap" rel="stylesheet">
<style>
  :root {
    --brand-blue: #0355a3;
    --brand-blue-dark: #0b4f9e;
    --brand-red: #9e2527;
    --accent-red: #eb1f27;
    --paper: #ffffff;
    --stage: #8f9094;
    --font: "Source Sans 3", sans-serif;
  }
  * { box-sizing: border-box; margin: 0; padding: 0; }
  html, body { width: 1200px; height: 1000px; overflow: hidden; }
  body { background: var(--stage); font-family: var(--font); position: relative; }

  .card { position: absolute; overflow: hidden; }

  /* Front */
  .card-front { left: 48px; top: 44px; width: 630px; height: 388px; background: var(--paper); }
  .front-brand { position: absolute; left: 38px; top: 40px; display: flex; align-items: center; gap: 22px; }
  .brand-dot { width: 116px; height: 116px; border-radius: 50%; background: var(--brand-blue); }
  .brand-name { color: var(--brand-blue); font-weight: 700; font-size: 44px; line-height: 1; letter-spacing: -0.5px; }
  .dotted-rule { position: absolute; left: 22px; right: 22px; border-top: 2px dotted var(--accent-red); }
  .rule-top { top: 162px; }
  .rule-bottom { top: 287px; }
  .person { position: absolute; left: 38px; top: 172px; color: var(--brand-blue); }
  .person-name { font-size: 32px; font-weight: 400; }
  .person-role { font-size: 20px; margin-top: 2px; }
  .contact { position: absolute; left: 283px; top: 172px; color: var(--brand-blue); font-size: 15.5px; line-height: 21.5px; list-style: none; }
  .front-band { position: absolute; left: 0; bottom: 0; width: 100%; height: 84px; background: var(--brand-blue-dark); display: flex; align-items: center; padding-left: 42px; }
  .front-web { color: var(--paper); font-size: 30px; letter-spacing: 0.5px; }

  /* Back */
  .card-back { left: 450px; top: 510px; width: 627px; height: 386px; background: var(--brand-red); }
  .back-base { position: absolute; left: 0; bottom: 0; width: 100%; height: 84px; background: var(--brand-blue-dark); }
  .back-badge { position: absolute; right: 0; top: 21px; width: 247px; height: 50px; background: var(--paper); display: flex; align-items: center; gap: 8px; padding-left: 12px; }
  .badge-dot { width: 32px; height: 32px; border-radius: 50%; background: var(--brand-blue); flex: none; }
  .badge-name { color: var(--brand-blue); font-weight: 700; font-size: 17px; white-space: nowrap; }
  .tagline { position: absolute; left: 47px; top: 76px; color: var(--paper); }
  .tagline-main { font-size: 42px; line-height: 1.05; font-weight: 400; letter-spacing: 0.5px; }
  .tagline-sub { font-size: 32px; line-height: 1.1; letter-spacing: 0.5px; }
  .back-web { margin-top: 8px; font-size: 22px; letter-spacing: 0.5px; }
  .brand-strip { position: absolute; left: 23px; top: 238px; width: 581px; height: 99px; background: var(--paper); display: flex; align-items: center; justify-content: space-around; padding: 0 10px; }
  .sub-brand { color: var(--brand-blue); font-weight: 700; font-size: 19px; white-space: nowrap; }
</style>
</head>
<body>

<section class="card card-front" aria-label="Business card front">
  <div class="front-brand">
    <span class="brand-dot"></span>
    <span class="brand-name">ROWAN PELLET GROUP</span>
  </div>
  <div class="dotted-rule rule-top"></div>
  <div class="person">
    <p class="person-name">Rowan Pellet</p>
    <p class="person-role">Principal</p>
  </div>
  <ul class="contact">
    <li>Phone:&nbsp; +61 2 5550 1420</li>
    <li>Phone:&nbsp; +61 400 555 218</li>
    <li>Email: Rowan@RowanPelletGroup.com.au</li>
    <li>PO Box 410, Belconnen ACT 2617,</li>
    <li>Australia</li>
  </ul>
  <div class="dotted-rule rule-bottom"></div>
  <div class="front-band">
    <span class="front-web">www.RowanPelletGroup.com.au</span>
  </div>
</section>

<section class="card card-back" aria-label="Business card back">
  <div class="back-base"></div>
  <div class="back-badge">
    <span class="badge-dot"></span>
    <span class="badge-name">ROWAN PELLET GROUP</span>
  </div>
  <div class="tagline">
    <p class="tagline-main">Event, travel and</p>
    <p class="tagline-sub">talent management</p>
    <p class="back-web">www.RowanPelletGroup.com.au</p>
  </div>
  <div class="brand-strip">
    <span class="sub-brand">RP Sports Tours</span>
    <span class="sub-brand">RP Events</span>
    <span class="sub-brand">RPG Management</span>
    <span class="sub-brand">Bold Mosaic</span>
  </div>
</section>

</body>
</html>
```